Flyer for Septic Pump Out Company

Ridgeway Tank Clearing – Septic Pump Out Services in Shoalhaven, NSW

Contact Details:
- Website: [www.ridgewaytankclearing-example.com.au]
- Phone: 0491 273 615
- Email: info@ridgewaytankclearing-example.com
- NSW Plumbers Licence: 318046K

At Ridgeway Tank Clearing, we provide professional and reliable septic tank pump-out services in Shoalhaven, NSW. Our team of Vac-Tanker Operators and licensed plumbers ensures that each service call is handled with the highest level of expertise and care. We are available 24/7 to meet your needs.

Our Services Include:
- Septic tank pump-outs
- Grease trap maintenance
- Winery and brewery waste management
- Aerobic treatment units (ATUs)
- Portable toilet pump-outs
- Stormwater removal
- Blockage clearing

With two purpose-built 12,000-litre vacuum trucks, capable of pumping liquids and sludge from depths up to 8 metres, we can access most septic tanks and grease traps with ease. Our compact design and 50-metre hose ensure that no job is too difficult for us to handle.

Why Maintain Your Septic System?

1. Save Money:Regular pump-outs are far more cost-effective than repairing or replacing a damaged system.
2. Prevent Health Hazards: Properly maintained septic systems reduce environmental and health risks, preventing groundwater contamination and safeguarding drinking water.
3. Property Value: A well-maintained septic system preserves the value of your property and ensures no delays in potential sales.

Signs of a Failing Septic System:
- Sewage surfacing over the drainfield
- Lush, green growth or soggy areas over the drainfield
- Slow or backed-up drains, toilets, or sinks
- Foul sewage odours around your property
- Poor well water test results

If you notice any of these signs, call us for a thorough system assessment. We can diagnose and clear blockages, assess the health of your septic system, and provide expert advice on long-term solutions.

What to Do If You Have a Septic Problem:

- Contact Ridgeway Tank Clearing:We'll assess the issue and recommend a solution. In many cases, a thorough pump-out will resolve the problem.
- Schedule Regular Maintenance: We recommend pumping your septic tank regularly and are happy to schedule follow-ups as needed—every 3 years is typical.
- Conserve Water: If your system hasn’t completely failed, water-saving measures can help alleviate stress on the system in the short term.
- Fence Off Problem Areas: If effluent is surfacing, make sure to fence off the affected area to keep people and pets safe.

At Ridgeway Tank Clearing, we’re committed to delivering prompt, dependable service at competitive prices. Whether it’s a routine maintenance job or an emergency, our team is here to help.

```html
<!DOCTYPE html>
<html lang="en">
<head>
<meta charset="utf-8">
<title>Ridgeway Tank Clearing – Septic Pump Out Flyer</title>
<link rel="stylesheet" href="https://fonts.googleapis.com/css2?family=Arimo:ital,wght@0,400;0,700;1,400;1,700&family=Oswald:wght@500;600&display=swap">
<style>
:root{
  --navy:#24347f;
  --blue-mid:#2a62b0;
  --blue-light:#1f9ad8;
  --green:#045a2e;
  --lime:#7bc143;
  --paper:#ffffff;
  --paper-grey:#f1f1f1;
  --ink:#2b2b2b;
  --backdrop:#d5d6d8;
  --grass-a:#5f9b3a;
  --grass-b:#9cc96a;
}
*{box-sizing:border-box;margin:0;padding:0}
html,body{width:1200px;height:800px;overflow:hidden}
body{background:var(--backdrop);font-family:"Arimo",Arial,sans-serif;color:var(--ink);position:relative}
.spread{position:absolute;left:230px;width:740px;height:370px;display:flex;box-shadow:0 4px 14px rgba(0,0,0,.18)}
.spread--outer{top:18px}
.spread--inner{top:410px}
.page{position:relative;width:370px;height:370px;overflow:hidden}
.abs{position:absolute}
.photo{position:absolute;background:linear-gradient(160deg,var(--grass-b),var(--grass-a))}
.blue-panel{position:absolute;background:linear-gradient(170deg,var(--navy) 0%,var(--blue-mid) 45%,var(--blue-light) 100%)}

/* back panel */
.back{background:var(--green)}
.back .photo{left:0;top:0;width:370px;height:175px}
.back .blue-panel{left:22px;top:105px;width:348px;height:245px;clip-path:polygon(0 22%,100% 0,100% 100%,0 100%)}
.brand-tile{position:absolute;left:48px;top:36px;width:120px;height:112px;background:var(--paper);display:flex;flex-direction:column;align-items:center;justify-content:center;gap:6px;padding:8px}
.brand-tile .dot{width:26px;height:26px;border-radius:50%;background:var(--blue-mid)}
.brand-name{font-weight:700;color:var(--green);font-size:15px;line-height:1.1;text-align:center}
.back-intro{left:60px;top:178px;width:280px;font-size:10.5px;line-height:1.35;text-align:center;color:#fff}
.contact{left:58px;top:258px;border-left:1.5px solid var(--lime);padding-left:12px}
.contact h3{font-style:italic;font-weight:700;font-size:15px;color:var(--lime);margin-bottom:5px}
.contact li{list-style:none;display:flex;align-items:center;gap:6px;font-size:10px;color:#fff;line-height:1.55}
.contact svg{width:10px;height:10px;flex:none}

/* front cover */
.front{background:var(--green)}
.front .photo{left:0;top:0;width:370px;height:150px}
.front .blue-panel{left:0;top:62px;width:335px;height:245px;clip-path:polygon(0 12%,88% 0,100% 100%,0 100%)}
.corner-white{position:absolute;right:0;bottom:0;width:95px;height:100px;background:var(--paper);clip-path:polygon(40% 0,100% 0,100% 100%,0 100%)}
.cover-brand{left:40px;top:98px;display:flex;align-items:center;gap:8px}
.cover-brand .square{width:14px;height:14px;background:#fff}
.cover-brand span{font-weight:700;font-size:17px;color:#fff}
.cover-title{left:40px;top:152px;font-family:"Oswald",sans-serif;color:#fff;text-transform:uppercase;line-height:1.15}
.cover-title strong{display:block;font-weight:600;font-size:21px}
.cover-title em{display:block;font-style:normal;font-weight:500;font-size:14px}
.underline{height:3px;width:70px;background:var(--lime);margin-top:4px}
.cover-intro{left:40px;top:222px;width:255px;font-size:9.5px;line-height:1.35;color:#fff}

/* inner left */
.inner-left{background:var(--paper-grey)}
.grey-block{left:0;top:0;width:120px;height:40px;background:#e4e4e4}
.green-strip{left:0;top:40px;width:10px;height:100px;background:var(--green)}
.green-top{left:130px;top:0;width:240px;height:18px;background:var(--green);clip-path:polygon(55% 0,100% 0,100% 100%,50% 100%)}
.sheet-white{left:12px;top:18px;width:358px;height:230px;background:var(--paper)}
.h-section{font-weight:700;font-size:15px;line-height:1.15;color:var(--ink)}
.h-section span{color:var(--green)}
.h-section::after{content:"";display:block;width:40px;height:2.5px;background:var(--lime);margin-top:4px}
.why{left:30px;top:32px;width:300px}
.why ol{list-style:none;margin-top:8px}
.why li{margin-bottom:7px}
.why b{display:block;font-size:11px;margin-bottom:2px}
.why p{font-size:9px;line-height:1.3}
.inner-left .blue-panel{left:0;top:200px;width:370px;height:170px;clip-path:polygon(0 0,100% 50%,100% 100%,0 100%)}
.services{left:22px;top:240px}
.services h3{font-weight:700;font-size:14px;color:#fff;margin-bottom:6px}
.services li{list-style:none;font-size:9px;color:#fff;line-height:1.45}
.inner-left .photo.truck{left:200px;top:222px;width:145px;height:138px;clip-path:polygon(0 0,100% 22%,100% 100%,0 100%);background:linear-gradient(170deg,#7e9fb9,#8aa86a 60%,#5f8d3a)}

/* inner right */
.inner-right{background:var(--green)}
.inner-right .sheet-white{left:0;top:32px;width:355px;height:320px;background:var(--paper-grey)}
.navy-band{left:0;top:30px;width:355px;height:58px;background:var(--navy);clip-path:polygon(0 14%,100% 0,100% 100%,0 100%);padding:12px 14px 0 16px;font-style:italic;font-size:8px;line-height:1.3;color:#fff}
.signs{left:16px;top:96px;width:330px}
.signs .h-section{font-size:14px}
.signs ul{list-style:none;margin-top:5px}
.signs li{font-style:italic;font-weight:700;font-size:9px;line-height:1.45;padding-left:11px;position:relative}
.signs li::before{content:"";position:absolute;left:0;top:3.5px;border-left:5px solid var(--lime);border-top:3px solid transparent;border-bottom:3px solid transparent}
.signs p{font-style:italic;font-size:8.5px;line-height:1.25;margin-top:4px}
.inner-right .blue-panel{left:0;top:226px;width:355px;height:138px;clip-path:polygon(0 9%,100% 0,100% 100%,0 100%)}
.todo{left:16px;top:240px;width:200px}
.todo h3{font-style:italic;font-weight:700;font-size:9.5px;color:#fff;white-space:nowrap}
.todo h3::after{content:"";display:block;width:36px;height:2px;background:var(--lime);margin:2px 0 3px}
.todo b{display:block;font-style:italic;font-size:8px;line-height:1.1;color:#fff}
.todo p{font-style:italic;font-size:6.5px;line-height:1.25;color:#fff;margin-bottom:1px}
.inner-right .photo.hose{left:222px;top:240px;width:123px;height:112px;background:linear-gradient(160deg,#3a5f92,#7fae55 55%,#5c8f38)}
</style>
</head>
<body>

<section class="spread spread--outer">
  <div class="page back">
    <div class="photo" role="img" aria-label="Worker in boots laying a suction hose across a green lawn"></div>
    <div class="blue-panel"></div>
    <div class="brand-tile">
      <div class="dot"></div>
      <div class="brand-name">Ridgeway Tank Clearing</div>
    </div>
    <p class="abs back-intro">At Ridgeway Tank Clearing, we’re committed to delivering prompt, dependable service at competitive prices. Whether it’s a routine maintenance job or an emergency, our team is here to help.</p>
    <div class="abs contact">
      <h3>Get In Touch!</h3>
      <ul>
        <li><svg viewBox="0 0 10 10"><rect x="1.5" y="1" width="7" height="8" rx="1" fill="none" stroke="#fff"/><line x1="3.5" y1="7.5" x2="6.5" y2="7.5" stroke="#fff"/></svg>0491 273 615</li>
        <li><svg viewBox="0 0 10 10"><circle cx="5" cy="5" r="4" fill="none" stroke="#fff"/><ellipse cx="5" cy="5" rx="1.8" ry="4" fill="none" stroke="#fff"/><line x1="1" y1="5" x2="9" y2="5" stroke="#fff"/></svg>www.ridgewaytankclearing-example.com.au</li>
        <li><svg viewBox="0 0 10 10"><rect x="1" y="2" width="8" height="6" fill="none" stroke="#fff"/><polyline points="1,2 5,5.5 9,2" fill="none" stroke="#fff"/></svg>info@ridgewaytankclearing-example.com</li>
        <li><svg viewBox="0 0 10 10"></svg>NSW Plumbers Licence: 318046K</li>
      </ul>
    </div>
  </div>

  <div class="page front">
    <div class="photo" role="img" aria-label="Close view of a worker kneeling on grass holding a corrugated suction hose"></div>
    <div class="blue-panel"></div>
    <div class="corner-white"></div>
    <div class="abs cover-brand"><div class="square"></div><span>Ridgeway Tank Clearing</span></div>
    <h1 class="abs cover-title"><strong>Septic Pump Out Services</strong><em>in Shoalhaven, NSW</em><div class="underline"></div></h1>
    <p class="abs cover-intro">At Ridgeway Tank Clearing, we provide professional and reliable septic tank pump-out services in Shoalhaven, NSW. Our team of Vac-Tanker Operators and licensed plumbers ensures that each service call is handled with the highest level of expertise and care. We are available 24/7 to meet your needs.</p>
  </div>
</section>

<section class="spread spread--inner">
  <div class="page inner-left">
    <div class="abs grey-block"></div>
    <div class="abs green-top"></div>
    <div class="abs sheet-white"></div>
    <div class="abs green-strip"></div>
    <div class="abs why">
      <h2 class="h-section">Why Maintain Your<br><span>Septic System?</span></h2>
      <ol>
        <li><b>1. Save Money</b><p>Regular pump-outs are far more cost-effective than repairing or replacing a damaged system.</p></li>
        <li><b>2. Prevent Health Hazards</b><p>Properly maintained septic systems reduce environmental and health risks, preventing groundwater contamination and safeguarding drinking water.</p></li>
        <li><b>3. Property Value</b><p>A well-maintained septic system preserves the value of your property and ensures no delays in potential sales.</p></li>
      </ol>
    </div>
    <div class="blue-panel"></div>
    <div class="abs services">
      <h3>Services Include:</h3>
      <ul>
        <li>Septic tank pump-outs</li>
        <li>Grease trap maintenance</li>
        <li>Winery and brewery waste management</li>
        <li>Aerobic treatment units (ATUs)</li>
        <li>Portable toilet pump-outs</li>
        <li>Stormwater removal</li>
        <li>Blockage clearing</li>
      </ul>
    </div>
    <div class="photo truck" role="img" aria-label="Vacuum tanker truck on a lawn with an operator guiding a green hose"></div>
  </div>

  <div class="page inner-right">
    <div class="abs sheet-white"></div>
    <div class="abs navy-band">With two purpose-built 12,000-litre vacuum trucks, capable of pumping liquids and sludge from depths up to 8 metres, we can access most septic tanks and grease traps with ease. Our compact design and 50-metre hose ensure that no job is too difficult for us to handle.</div>
    <div class="abs signs">
      <h2 class="h-section">Signs of a Failing <span>Septic System</span></h2>
      <ul>
        <li>Sewage surfacing over the drainfield</li>
        <li>Lush, green growth or soggy areas over the drainfield</li>
        <li>Slow or backed-up drains, toilets, or sinks</li>
        <li>Foul sewage odours around your property</li>
        <li>Poor well water test results</li>
      </ul>
      <p>If you notice any of these signs, call us for a thorough system assessment. We can diagnose and clear blockages, assess the health of your septic system, and provide expert advice on long-term solutions.</p>
    </div>
    <div class="blue-panel"></div>
    <div class="abs todo">
      <h3>What to Do If You Have a Septic Problem</h3>
      <b>Contact Ridgeway Tank Clearing</b>
      <p>We’ll assess the issue and recommend a solution. In many cases, a thorough pump-out will resolve the problem.</p>
      <b>Schedule Regular Maintenance</b>
      <p>We recommend pumping your septic tank regularly and are happy to schedule follow-ups as needed—every 3 years is typical.</p>
      <b>Conserve Water</b>
      <p>If your system hasn’t completely failed, water-saving measures can help alleviate stress on the system in the short term.</p>
      <b>Fence Off Problem Areas</b>
      <p>If effluent is surfacing, make sure to fence off the affected area to keep people and pets safe.</p>
    </div>
    <div class="photo hose" role="img" aria-label="Gloved worker lowering a suction hose into an open septic tank on grass"></div>
  </div>
</section>

</body>
</html>
```